Roll label Flyer design

I need a flyer for a roll label printer
Pictures for the project are located here:
https://plimtonstickers.sharefile.com/d-k4wq7812m3a0z551

Text I want is located here:
https://plimtonstickers.com/roll-labels.php

Target Market(s)

Manufactures, wholesalers

Industry/Entity Type

Printing

Requirements
Must have
• Lots of pictures. Our phone number 800-472-8164. Website www.plimtonstickers.com

```html
<!DOCTYPE html>
<html lang="en">
<head>
<meta charset="utf-8">
<title>Plimton Stickers – Roll Label Flyer</title>
<link href="https://fonts.googleapis.com/css2?family=Lato:wght@400;700;900&display=swap" rel="stylesheet">
<style>
  :root{
    --red:#c1272d;
    --red-dark:#9e1b20;
    --charcoal:#1f1f21;
    --ink:#1a1a1a;
    --paper:#f4f1f0;
    --backdrop:#b3b3b3;
    --white:#ffffff;
  }
  *{margin:0;padding:0;box-sizing:border-box}
  html,body{width:1200px;height:590px;overflow:hidden;background:var(--backdrop)}
  .stage{position:relative;width:1200px;height:590px;display:flex;justify-content:center;align-items:center}
  .flyer-frame{width:456px;height:590px;overflow:hidden;position:relative;box-shadow:0 4px 14px rgba(0,0,0,.25)}
  .flyer{position:absolute;top:0;left:0;width:570px;height:738px;transform:scale(.8);transform-origin:0 0;
    font-family:'Lato',sans-serif;color:var(--ink);background:var(--paper)}
  .flyer-art{position:absolute;inset:0;width:570px;height:738px}
  .brand{position:absolute;left:16px;top:24px;display:flex;align-items:center;gap:12px}
  .brand-dot{width:36px;height:36px;border-radius:50%;background:var(--red)}
  .brand-name{font-weight:700;font-size:17px;letter-spacing:3.5px;color:var(--white);text-transform:uppercase}
  .headline{position:absolute;left:318px;top:106px;width:236px;text-align:center;color:var(--white);
    font-weight:900;font-size:29px;line-height:1.03;text-transform:uppercase;text-shadow:0 1px 2px rgba(0,0,0,.2)}
  .headline span{display:block}
  .headline .gap{margin-top:10px}
  .copy{position:absolute;left:14px;top:334px;width:410px}
  .copy h2{color:var(--red);font-weight:700;font-size:18px;margin-bottom:4px}
  .copy p{font-size:10.6px;line-height:1.45;width:410px}
  .copy h3{color:var(--red);font-weight:700;font-size:13.5px;margin-top:8px;margin-bottom:2px}
  .copy ul{list-style:none;font-size:10.5px;line-height:15.3px}
  .copy li{padding-left:13px;position:relative}
  .copy li::before{content:"";position:absolute;left:2px;top:5px;width:6px;height:6px;border-radius:50%;background:var(--red)}
  .phone{position:absolute;left:14px;top:622px;font-weight:700;font-size:37px;letter-spacing:-.3px;color:var(--ink)}
  .website{position:absolute;left:14px;top:695px;font-weight:700;font-size:17px;color:var(--white)}
</style>
</head>
<body>
<main class="stage">
  <div class="flyer-frame">
    <article class="flyer">
      <svg class="flyer-art" viewBox="0 0 570 738">
        <defs>
          <linearGradient id="photoTones" x1="0" y1="0" x2="1" y2="1">
            <stop offset="0" stop-color="#c9c4bd"/>
            <stop offset=".5" stop-color="#6d6a68"/>
            <stop offset="1" stop-color="#a89e96"/>
          </linearGradient>
          <linearGradient id="pressTones" x1="0" y1="0" x2="1" y2="1">
            <stop offset="0" stop-color="#d8d8da"/>
            <stop offset="1" stop-color="#5c5e64"/>
          </linearGradient>
          <linearGradient id="paperSweep" x1="0" y1="0" x2="1" y2="1">
            <stop offset="0" stop-color="#ffffff"/>
            <stop offset=".6" stop-color="#f7ebe8"/>
            <stop offset="1" stop-color="#efe2df"/>
          </linearGradient>
        </defs>
        <rect class="body-panel" x="0" y="290" width="570" height="448" fill="url(#paperSweep)"/>
        <polygon class="header-red" points="0,0 570,0 570,318 40,300 0,322" fill="var(--red)"/>
        <polygon class="header-dark" points="0,0 570,0 0,130" fill="var(--charcoal)"/>
        <g role="img" aria-label="Photo of a press operator working at a roll label printing machine">
          <polygon points="10,128 310,60 310,300 40,300 10,280" fill="url(#photoTones)"/>
        </g>
        <polygon class="header-shadow" points="0,322 40,300 570,318 570,334 60,310" fill="var(--red-dark)" opacity=".6"/>
        <g role="img" aria-label="Close-up photos of printed roll labels running through press machinery">
          <polygon points="300,465 335,402 410,402 445,465 410,528 335,528" fill="url(#pressTones)"/>
          <polygon points="420,342 452,335 570,335 570,462 452,462 440,400" fill="url(#pressTones)"/>
          <polygon points="300,605 330,542 410,542 445,605 410,668 330,668" fill="url(#pressTones)"/>
          <polygon points="420,536 450,475 570,475 570,598 450,598" fill="url(#pressTones)"/>
          <polygon points="420,672 450,612 570,612 570,738 430,738" fill="url(#pressTones)"/>
        </g>
        <polygon class="footer-band" points="0,676 400,676 440,738 0,738" fill="var(--red)"/>
      </svg>

      <header class="brand">
        <span class="brand-dot"></span>
        <span class="brand-name">Plimton Stickers</span>
      </header>

      <h1 class="headline">
        <span>Outstanding</span>
        <span>Customer</span>
        <span>Service,</span>
        <span class="gap">Competitive</span>
        <span>Pricing</span>
      </h1>

      <section class="copy">
        <h2>Roll/Product Labels</h2>
        <p>Long or short run. Digital or flexographic. Standard shapes or unique, custom diecuts. Simple spot colors or full color with every embellishment. Let us help you create the perfect label for your application.</p>
        <h3>Features:</h3>
        <ul class="features">
          <li>Foil-Stamping</li>
          <li>Embossing</li>
          <li>Spot Varnishes</li>
          <li>Instant Redeemable Coupons</li>
          <li>Expanded Content/Booklet Labels</li>
        </ul>
        <h3>Specialty Markets We Service Include:</h3>
        <ul class="markets">
          <li>Health &amp; Beauty</li>
          <li>Food &amp; Beverage</li>
          <li>Wine &amp; Spirits</li>
          <li>Industrial Safety &amp; Warning</li>
          <li>Promotional</li>
          <li>Compliance (I.E. Safety Listings, California Prop 65)</li>
        </ul>
      </section>

      <p class="phone">800-472-8164</p>
      <p class="website">www.plimtonstickers.com</p>
    </article>
  </div>
</main>
</body>
</html>
```